Wedding Thank You post card

We would like to design a thank you post card for our wedding guests.
We want it to be a classic style with our photo and a simple 'Thank you' written and then Tom and Sylvia 15.03.2014' Where the writing does not obstruct our image.
We need 140 post cards
Sorry for the delay please find some photos you can use for the design process. One or all photos can be used. Thank you
Wedding

```html
<!DOCTYPE html>
<html lang="en">
<head>
<meta charset="utf-8">
<title>Tom and Sylvia – Thank You Postcard</title>
<link rel="stylesheet" href="https://fonts.googleapis.com/css2?family=Allura&family=Bodoni+Moda:wght@400&family=Questrial&display=swap">
<style>
  :root {
    --page: #ffffff;
    --card-border: #4a4a4a;
    --label: #555555;
    --names: #6b6b6b;
    --script-green: #c3d97a;
    --rule: #9a9a9a;
    --stamp: #7a7a7a;
  }
  html, body {
    margin: 0;
    padding: 0;
    width: 1200px;
    height: 1173px;
    overflow: hidden;
    background: var(--page);
  }
  .canvas {
    position: relative;
    width: 1200px;
    height: 1173px;
  }
  .side-label {
    position: absolute;
    left: 241px;
    margin: 0;
    font-family: "Questrial", sans-serif;
    font-size: 25px;
    font-weight: 400;
    color: var(--label);
    line-height: 1;
  }
  .side-label--front { top: 16px; }
  .side-label--back { top: 594px; }

  .postcard {
    position: absolute;
    left: 234px;
    width: 721px;
    border: 1px solid var(--card-border);
    background: var(--page);
    box-sizing: content-box;
  }
  .postcard--front { top: 44px; height: 527px; }
  .postcard--back { top: 622px; height: 529px; }

  .photo {
    position: absolute;
  }
  .photo--kiss-veil { left: 19px; top: 17px; width: 257px; height: 181px;
    background: linear-gradient(160deg, #e9eef1 0%, #d8dde0 45%, #6b5a4c 75%, #2f3240 100%); }
  .photo--couple-bouquet { left: 286px; top: 17px; width: 153px; height: 181px;
    background: linear-gradient(180deg, #c9d9e6 0%, #b9b2a6 40%, #4a4d5a 70%, #ece9e4 100%); }
  .photo--red-door { left: 449px; top: 17px; width: 257px; height: 181px;
    background: linear-gradient(90deg, #d7383c 0%, #b0a48f 30%, #8f8b80 60%, #c3c0b7 100%); }
  .photo--steps-party { left: 19px; top: 327px; width: 257px; height: 181px;
    background: linear-gradient(180deg, #8d8a80 0%, #a89f8f 35%, #7dbd6a 65%, #c7304a 100%); }
  .photo--castle-lawn { left: 286px; top: 327px; width: 153px; height: 181px;
    background: linear-gradient(180deg, #cfe0ef 0%, #a99c80 35%, #a7b85a 55%, #4c4a4a 80%, #e9e7e3 100%); }
  .photo--guests { left: 449px; top: 327px; width: 257px; height: 181px;
    background: linear-gradient(180deg, #c4cdd6 0%, #8a877d 40%, #5b4d6a 65%, #55565a 100%); }

  .lettering {
    position: absolute;
    left: 0;
    top: 200px;
    width: 721px;
    height: 80px;
    overflow: visible;
  }
  .lettering__script {
    font-family: "Allura", cursive;
    font-size: 96px;
    fill: var(--script-green);
  }
  .lettering__swash {
    fill: none;
    stroke: var(--script-green);
    stroke-width: 2;
  }

  .couple {
    position: absolute;
    margin: 0;
    text-align: center;
    font-family: "Bodoni Moda", serif;
    color: var(--names);
    line-height: 21px;
  }
  .couple__names { display: block; font-size: 19px; letter-spacing: 0.3px; }
  .couple__date { display: block; font-size: 18px; }
  .postcard--front .couple { left: 210px; width: 305px; top: 275px; }
  .postcard--back .couple { left: 30px; width: 300px; top: 31px; }

  .photo--pub-toast { left: 68px; top: 83px; width: 221px; height: 155px;
    background: linear-gradient(135deg, #3b2418 0%, #8b5a34 40%, #d8c6a8 60%, #4a2a1a 100%); }

  .divider {
    position: absolute;
    left: 361px;
    top: 85px;
    width: 1px;
    height: 413px;
    background: var(--rule);
  }
  .stamp-box {
    position: absolute;
    left: 613px;
    top: 25px;
    width: 87px;
    height: 96px;
    border: 1px solid var(--stamp);
  }
  .address-line {
    position: absolute;
    left: 395px;
    width: 274px;
    height: 1px;
    background: var(--rule);
  }
  .address-line--1 { top: 323px; }
  .address-line--2 { top: 376px; }
  .address-line--3 { top: 430px; }
</style>
</head>
<body>
<main class="canvas">
  <h2 class="side-label side-label--front">front</h2>
  <section class="postcard postcard--front">
    <div class="photo photo--kiss-veil" role="img" aria-label="Photo of the bride and groom kissing, her veil blowing in the wind"></div>
    <div class="photo photo--couple-bouquet" role="img" aria-label="Photo of the couple smiling, the bride holding a white bouquet"></div>
    <div class="photo photo--red-door" role="img" aria-label="Photo of the couple on the steps before a red castle door"></div>

    <svg class="lettering" viewBox="0 0 721 80" aria-label="love &amp; thanks">
      <path class="lettering__swash" d="M0 50 C 40 46, 80 60, 110 60 M600 55 C 650 44, 690 44, 721 54"/>
      <text class="lettering__script" x="360" y="66" text-anchor="middle" textLength="520" lengthAdjust="spacingAndGlyphs">love &amp; thanks</text>
    </svg>

    <p class="couple">
      <span class="couple__names">TOM AND SYLVIA</span>
      <span class="couple__date">March 15, 2014</span>
    </p>

    <div class="photo photo--steps-party" role="img" aria-label="Photo of the couple and bridesmaids in green sitting on castle steps"></div>
    <div class="photo photo--castle-lawn" role="img" aria-label="Photo of the couple kissing on a drive before a castle"></div>
    <div class="photo photo--guests" role="img" aria-label="Photo of the couple kissing with all the wedding guests behind them"></div>
  </section>

  <h2 class="side-label side-label--back">back</h2>
  <section class="postcard postcard--back">
    <p class="couple">
      <span class="couple__names">TOM AND SYLVIA</span>
      <span class="couple__date">March 15, 2014</span>
    </p>
    <div class="photo photo--pub-toast" role="img" aria-label="Photo of the couple drinking stout at a wood-panelled bar"></div>
    <div class="divider"></div>
    <div class="stamp-box"></div>
    <div class="address-line address-line--1"></div>
    <div class="address-line address-line--2"></div>
    <div class="address-line address-line--3"></div>
  </section>
</main>
</body>
</html>
```